Word Document Estimate Sheet

Good evening. I have an home renovations company that does a lot of estimates through word documents and then emailed them a PDF document. ArtHarbor did my logo and stationary projects and did a great job with it. Now I need my word document estimate sheet to be more standardized meaning sometimes my headers and footers move when I get to the bottom of the page , this make me have to do a copy and paste many times to put them back in their place also I have headings like Master Bedroom, Master Bath . I would like for them to always be bold, underlined and colon on the end now I always have to do this. I would like for the header and footers to not move when I get to the bottom of the page. Basically I want the same document with the same look as the document I send but with less retyping and copy and pasting. Hopefully this makes sense and you can help my estimates go faster.

Thanks,
Glen

Target Market(s)

Customer who want an estimate

Industry/Entity Type

It Company

Requirements
Must have
• 1.Must have same header and footer as the document I sent but want text to be standard.
• 2.Header and footer must not move when I get to the bottom of page.
• 3.Categories like Master Bedroom, Kitchen Area categories must already be in the document and if I want to delete them I can.
Nice to have
• I would love my estimate time to be cut in half because new word estimate sheet is simple to work with.
Should not have
• Don't change the header and footer design at all just make sure it doesn't move when I type.

```html
<!DOCTYPE html>
<html lang="en">
<head>
<meta charset="utf-8">
<title>Estimate Sheet – Calder Home Renovations</title>
<link href="https://fonts.googleapis.com/css2?family=Tinos:wght@400;700&display=swap" rel="stylesheet">
<style>
  :root {
    --backdrop: #9a9a9a;
    --paper: #ffffff;
    --header-grey: #e6e7e9;
    --navy: #170a4a;
    --ink: #111111;
    --note-red: #e8141b;
    --accent-gold: #d9a82b;
    --divider: #c9c9c9;
  }
  * { box-sizing: border-box; }
  html, body {
    margin: 0;
    width: 1200px;
    height: 639px;
    overflow: hidden;
    background: var(--backdrop);
    font-family: "Tinos", "Times New Roman", serif;
    color: var(--ink);
  }
  .spread {
    position: absolute;
    left: 175px;
    top: 21px;
    display: flex;
  }
  .page {
    position: relative;
    width: 425px;
    height: 600px;
    background: var(--paper);
  }
  .page + .page { border-left: 1px solid var(--divider); }
  .page-header {
    height: 59px;
    background: var(--header-grey);
    display: flex;
    align-items: center;
    justify-content: center;
    gap: 5px;
    border-bottom: 7px solid var(--navy);
    height: 66px;
  }
  .brand-mark {
    width: 9px;
    height: 9px;
    background: var(--accent-gold);
  }
  .brand-name {
    font-weight: 700;
    font-size: 12px;
    color: var(--navy);
    letter-spacing: 0.3px;
  }
  .page-body {
    padding: 0 37px 0 31px;
    font-size: 10.4px;
    line-height: 13.6px;
  }
  .page-body.continued { padding-top: 18px; }
  .doc-title {
    margin: 16px 0 0;
    text-align: center;
    font-size: 17.6px;
    line-height: 20px;
    font-weight: 700;
    letter-spacing: 0.6px;
  }
  .client-address {
    margin: 10px 0 0 50px;
    display: flex;
    gap: 3px;
  }
  .client-address .label { font-weight: 700; font-size: 11.5px; }
  .client-address .lines { font-size: 10.4px; }
  .client-address .name { font-size: 11.5px; }
  .scope-title {
    margin: 13px 0 0;
    text-align: center;
    font-weight: 700;
    font-size: 11.5px;
    text-decoration: underline;
  }
  .area-heading {
    margin: 13px 0 0;
    font-weight: 700;
    font-size: 10.4px;
    text-decoration: underline;
  }
  .scope-title + .area-heading { margin-top: 1px; }
  .page-body.continued .area-heading:first-child { margin-top: 0; }
  .task-list {
    margin: 0;
    padding-left: 27px;
    list-style: disc;
  }
  .task-list li { margin-top: 13px; }
  .customer-note { color: var(--note-red); }
  .page-footer {
    position: absolute;
    left: 0;
    bottom: 0;
    width: 100%;
    height: 55px;
    background: var(--navy);
    color: #ffffff;
    text-align: center;
    font-size: 6.6px;
    line-height: 8.6px;
    padding-top: 13px;
  }
  .page-footer .sep { margin: 0 3px; }
</style>
</head>
<body>
<div class="spread">

  <section class="page">
    <header class="page-header">
      <span class="brand-mark"></span>
      <span class="brand-name">Calder Home Renovations</span>
    </header>
    <div class="page-body">
      <h1 class="doc-title">Licensed Bonded &amp; Insured</h1>
      <div class="client-address">
        <span class="label">Address:</span>
        <div class="lines">
          <div class="name">Darius Lowell</div>
          <div>58 Fenwick Lane</div>
          <div>Brookfield, NC 28004</div>
        </div>
      </div>
      <h2 class="scope-title">Scope of work:</h2>

      <h3 class="area-heading">Front Door:</h3>
      <ul class="task-list">
        <li>Clean &amp; paint both sides of door. (Interior semi-gloss white and outside satin black)</li>
        <li>Clean &amp; paint interior trim of front door &amp; foyer coat closet door (All 3 sides).</li>
      </ul>

      <h3 class="area-heading">Living Area:</h3>
      <ul class="task-list">
        <li>Clean &amp; paint all base molding in stated area a semi-gloss white color.</li>
        <li>Repair wood flooring in corner and matching quarter-round in stated area. <span class="customer-note">(Customer will supply quarter-round).</span></li>
        <li>Clean and paint 2.25 wide trim on both sides of opening going into kitchen.</li>
      </ul>

      <h3 class="area-heading">Kitchen Area:</h3>
      <ul class="task-list">
        <li>Paint kitchen/ hall ceiling a flat white color.</li>
        <li>Clean &amp; paint all base molding in stated area a semi-gloss white color.</li>
        <li>Clean and paint 2.25 wide trim at sliding glass door.</li>
      </ul>
    </div>
    <footer class="page-footer">
      <div>Nadia Calder&nbsp; OFFICE: 555-210-4471<span class="sep">|</span>Glen Calder&nbsp; CELL: 555-210-4472<span class="sep">|</span>EMAIL: glen@calderhomerenovations.com</div>
      <div>412 Harbor Ridge Rd., Suite 210 Brookfield, NC 28004</div>
      <div>www.calderhomerenovations.com</div>
    </footer>
  </section>

  <section class="page">
    <header class="page-header">
      <span class="brand-mark"></span>
      <span class="brand-name">Calder Home Renovations</span>
    </header>
    <div class="page-body continued">
      <h3 class="area-heading">Hallway:</h3>
      <ul class="task-list">
        <li>Clean &amp; paint all base molding in stated area a semi-gloss white color</li>
      </ul>

      <h3 class="area-heading">Washer &amp; Dryer Area:</h3>
      <ul class="task-list">
        <li>Clean &amp; paint all base molding in stated area a semi-gloss white color</li>
        <li>Clean both doors in stated area first and if it’s determined it needs to be painted we will discuss with customer for pricing before painting it.</li>
        <li>Clean and paint 2.25 wide trim on both sides of door’s.</li>
      </ul>

      <h3 class="area-heading">Hall Bath:</h3>
      <ul class="task-list">
        <li>Clean &amp; paint all base molding in stated area a semi-gloss white color</li>
        <li>Clean and paint 2.25 wide trim on both sides of door a semi-gloss white.</li>
        <li>Remove, replace and paint broken quarter-round at the base of tub.</li>
        <li>Clean both doors in stated area first and if it’s determined it needs to be painted we will discuss with customer for pricing before painting it.</li>
      </ul>

      <h3 class="area-heading">Master Bedroom:</h3>
      <ul class="task-list">
        <li>Clean &amp; paint all base molding in stated area a semi-gloss white color</li>
        <li>Clean and paint 2.25 wide trim on both sides of doors a semi-gloss white.</li>
        <li>Clean all three doors in stated area first and if it’s determined it needs to be painted we will discuss with customer for pricing before painting it.</li>
      </ul>
    </div>
    <footer class="page-footer">
      <div>Nadia Calder&nbsp; OFFICE: 555-210-4471<span class="sep">|</span>Glen Calder&nbsp; CELL: 555-210-4472<span class="sep">|</span>EMAIL: glen@calderhomerenovations.com</div>
      <div>412 Harbor Ridge Rd., Suite 210 Brookfield, NC 28004</div>
      <div>www.calderhomerenovations.com</div>
    </footer>
  </section>

</div>
</body>
</html>
```